Book Cover design: Waltz beside a Heron.

I need a front and back cover for my book called 'Waltz beside a Heron'.
It is self development book for help a person to be a better coach.
It is a metaphor. Dance is asking questions and the octopus is the person you are coaching (complex with my 'tentacles').
The audience would be adults. so want the cover to capture attention and also show that is have something of interest inside.
I have attach my first attempt. Please be bold.
The best sellers in this market place have simple but clear front page & back pages.

All the words are important but the sub-title is likely to change.

Target Market(s)

Adults who work with each other.
More business type people.

Industry/Entity Type

Leadership

Font styles to use
Serif

Requirements
Must have
• My project must have... The words that in the draft mock up.
• 'Waltz beside a Heron' [TITLE]
• 'A Map for Honest Mentoring'[SUB-TITLE]
• How to create inspiration and accountability using
• Five Critical Moments.[SUB_TITLE]
• By Godfrey T Haswell
Nice to have
• Clever and simple.

```html
<!DOCTYPE html>
<html lang="en">
<head>
<meta charset="utf-8">
<title>Waltz beside a Heron – Cover Spread</title>
<link rel="stylesheet" href="https://fonts.googleapis.com/css2?family=Bowlby+One+SC&family=Cinzel:wght@700&family=Libre+Baskerville:wght@700&family=Roboto+Condensed:wght@700&family=Roboto:ital,wght@1,900&display=swap">
<style>
  :root {
    --page: #ffffff;
    --cover: #bdd8d3;
    --cover-light: #c6dfda;
    --navy: #0d5286;
    --navy-dark: #0a4672;
    --title-shadow: #7fa7c4;
    --edge: #3a3a3a;
    --spine-text: #ffffff;
    --spine-outline: #111111;
  }
  html, body {
    margin: 0;
    padding: 0;
    width: 1200px;
    height: 1200px;
    overflow: hidden;
    background: var(--page);
  }
  .canvas {
    position: relative;
    width: 1200px;
    height: 1200px;
  }
  .spread {
    position: absolute;
    left: 66px;
    top: 200px;
    width: 1076px;
    height: 726px;
    background: radial-gradient(ellipse at 30% 50%, var(--cover-light), var(--cover) 70%);
    border: 1px solid var(--edge);
    box-sizing: border-box;
  }
  .spine {
    position: absolute;
    left: 511px;
    top: 0;
    width: 54px;
    height: 100%;
    background: var(--navy);
    border-left: 1px solid var(--edge);
    border-right: 1px solid var(--edge);
    box-sizing: border-box;
  }
  .spine-title {
    position: absolute;
    left: 50%;
    top: 50%;
    transform: translate(-50%, -50%) rotate(90deg);
    white-space: nowrap;
    font-family: "Roboto", Arial, sans-serif;
    font-style: italic;
    font-weight: 900;
    font-size: 34px;
    letter-spacing: 1px;
    color: var(--spine-text);
    -webkit-text-stroke: 2px var(--spine-outline);
    paint-order: stroke fill;
    text-shadow: 2px 2px 0 var(--spine-outline);
  }
  .front {
    position: absolute;
    left: 565px;
    top: 0;
    width: 510px;
    height: 100%;
    text-align: center;
    color: var(--navy);
  }
  .series-line {
    position: absolute;
    top: 30px;
    width: 100%;
    margin: 0;
    font-family: "Libre Baskerville", Georgia, serif;
    font-weight: 700;
    font-size: 19px;
  }
  .book-title {
    position: absolute;
    top: 92px;
    width: 100%;
    margin: 0;
    font-weight: normal;
  }
  .book-title span { display: block; }
  .title-big {
    font-family: "Bowlby One SC", Impact, sans-serif;
    font-size: 80px;
    line-height: 84px;
    color: var(--navy);
    text-shadow: 3px 3px 0 var(--title-shadow);
  }
  .title-mid {
    font-family: "Cinzel", Georgia, serif;
    font-weight: 700;
    font-size: 40px;
    line-height: 56px;
    letter-spacing: 12px;
    color: var(--navy-dark);
  }
  .title-last {
    font-family: "Bowlby One SC", Impact, sans-serif;
    font-size: 60px;
    line-height: 50px;
    letter-spacing: 3px;
    color: var(--navy);
    text-shadow: 3px 3px 0 var(--title-shadow);
  }
  .cover-art {
    position: absolute;
    left: 119px;
    top: 296px;
    width: 272px;
    height: 224px;
  }
  .tagline {
    position: absolute;
    top: 537px;
    width: 100%;
    margin: 0;
    font-family: "Roboto Condensed", "Arial Narrow", sans-serif;
    font-weight: 700;
    font-size: 19px;
    line-height: 27px;
    text-transform: uppercase;
  }
  .author {
    position: absolute;
    top: 680px;
    width: 100%;
    margin: 0;
    font-family: "Libre Baskerville", Georgia, serif;
    font-weight: 700;
    font-size: 14px;
    text-transform: uppercase;
  }
</style>
</head>
<body>
<div class="canvas">
  <div class="spread">
    <section class="back-cover" aria-label="Back cover"></section>

    <div class="spine">
      <div class="spine-title">WALTZ BESIDE A HERON</div>
    </div>

    <section class="front">
      <p class="series-line">A Map for Honest Mentoring</p>
      <h1 class="book-title">
        <span class="title-big">WALTZ</span>
        <span class="title-mid">BESIDE A</span>
        <span class="title-last">HERON</span>
      </h1>
      <svg class="cover-art" viewBox="0 0 272 224" role="img" aria-label="Line drawing of a smiling heron-like creature with curling limbs, set in an oval frame">
        <ellipse cx="136" cy="112" rx="133" ry="109" fill="#f4f6f6" stroke="var(--navy)" stroke-width="3"/>
      </svg>
      <p class="tagline">How to build<br>trust and steady follow-through using<br>five pivotal mentoring moments</p>
      <p class="author">Godfrey T Haswell</p>
    </section>
  </div>
</div>
</body>
</html>
```